Quendrix-Commons Theme For Forums!

We are looking for a theme for our forums. The forums are ran off Invision Power Boards. We have a basic theme on there now but we want more our own feel. If possible have some longboarding accept incorporated in the theme. We want the theme to have some red in it to match our logo. Quendrix-commons.net

Target Market(s)

Skatingboarding & Longboarding

Coding

Coded - Design and coding required

Number of Pages Required

1 page

Colors
f04a50

```html
<!DOCTYPE html>
<html lang="en">
<head>
<meta charset="utf-8">
<title>Quendrix-Commons</title>
<link href="https://fonts.googleapis.com/css2?family=Montserrat:wght@500;600;700;800&family=Open+Sans:wght@400;600;700&display=swap" rel="stylesheet">
<style>
:root{
  --dark:#353535;
  --red:#e2001a;
  --page:#ececee;
  --white:#ffffff;
  --band:#e6e6e7;
  --text:#222222;
  --line:#cfcfd2;
  --muted:#d8d8d8;
}
*{box-sizing:border-box;margin:0;padding:0}
html,body{width:1200px;height:1166px;overflow:hidden}
body{background:var(--page);font-family:"Open Sans",sans-serif;color:var(--text);font-size:11px;position:relative}
a{color:inherit}
.site-header{position:absolute;left:0;top:0;width:1200px;height:89px;background:var(--dark)}
.brand{position:absolute;left:133px;top:22px;font-family:"Montserrat",sans-serif;font-weight:800;font-size:26px;color:var(--white);letter-spacing:.5px;display:flex;align-items:center;gap:8px}
.brand .dot{width:14px;height:14px;background:var(--red)}
.account{position:absolute;right:132px;top:28px;display:flex;align-items:center;gap:7px;font-family:"Montserrat",sans-serif;color:var(--white);font-size:11.5px}
.avatar{width:25px;height:25px;border-radius:50%;background:#e9e9e9;margin-right:6px;display:flex;align-items:center;justify-content:center}
.greeting{margin-right:20px}
.btn-outline{border:1px solid #cfcfcf;padding:6px 13px;font-size:10.5px;color:var(--white)}
.nav{position:absolute;left:0;top:89px;width:1200px;height:32px;background:var(--white);box-shadow:0 1px 3px rgba(0,0,0,.08)}
.nav ul{list-style:none;position:absolute;right:132px;top:9px;display:flex;gap:0;font-family:"Montserrat",sans-serif;font-size:11.5px;font-weight:500}
.nav li{margin-left:34px}
.nav li:nth-child(4){margin-left:42px}
.main{position:absolute;left:132px;top:0;width:936px}
.page-title{position:absolute;left:0;top:144px;display:flex;align-items:flex-end;gap:4px;font-family:"Montserrat",sans-serif;font-weight:600;font-size:12.5px}
.welcome-bar{position:absolute;left:0;top:186px;width:936px;height:41px;background:var(--band);border:1px solid #dcdcde;display:flex;align-items:center;padding-left:13px;font-size:10.5px}
.welcome-bar em{font-style:normal;color:var(--red);margin-left:3px}
.login-form{position:absolute;right:8px;top:8px;display:flex;gap:7px}
.field{width:121px;height:24px;background:var(--white);border:1px solid #c9c9c9;font-size:9.5px;padding:6px 9px;line-height:1}
.field.pass{letter-spacing:2px;font-weight:700}
.go{width:34px;height:24px;background:var(--red);color:var(--white);font-family:"Montserrat",sans-serif;font-weight:700;font-size:11.5px;display:flex;align-items:center;justify-content:center;margin-left:-2px}
.cat-head{position:absolute;left:0;width:936px;height:31px;background:var(--red);color:var(--white);font-family:"Montserrat",sans-serif;font-weight:600;font-size:11.5px;display:flex;align-items:center;padding-left:9px;gap:6px}
.collapse{position:absolute;right:11px;top:9px;width:14px;height:14px;background:var(--white);border-radius:2px}
.collapse::after{content:"";position:absolute;left:3px;top:6px;width:8px;height:2px;background:var(--red)}
.forum-table{position:absolute;left:0;top:297px;width:936px;border-collapse:collapse;background:var(--white);box-shadow:0 1px 2px rgba(0,0,0,.1)}
.forum-table th{background:var(--dark);color:var(--white);font-weight:700;font-size:11.5px;height:28px;text-align:left;padding-left:21px;border-left:1px solid #555}
.forum-table th.num{text-align:center;padding-left:0}
.forum-table th:first-child{border-left:none}
.forum-table td{height:93px;border-left:1px solid var(--line);vertical-align:middle;font-size:11px}
.forum-table td:first-child{border-left:none}
.forum-table td.num{text-align:center}
.forum-cell{display:flex;align-items:center;padding-left:22px}
.forum-cell .icon{width:37px;height:37px;border-radius:50%;background:#ececec;border:1px solid #d5d5d5;display:flex;align-items:center;justify-content:center;margin-right:23px}
.forum-name{font-size:12px;font-weight:600;margin-bottom:5px}
.last-post{padding-left:17px;line-height:17.5px;font-size:10.5px}
.board-links{position:absolute;left:622px;top:473px;width:314px;height:32px;background:var(--band);border:1px solid #d0d0d2;border-bottom:none;font-size:10.5px;display:flex;align-items:center;justify-content:center;gap:11px}
.stats-nav{position:absolute;left:0;top:536px;width:936px;height:27px;background:var(--dark);color:var(--white);font-size:10.5px;font-weight:600;display:flex;align-items:center;justify-content:flex-end;padding-right:16px;gap:13px}
.stats-nav .sep{width:4px;height:4px;border-radius:50%;background:var(--white)}
.row{position:absolute;left:0;width:936px}
.row.band{background:var(--band);padding-left:17px;font-size:11.5px;display:flex;align-items:center}
.row.body{background:var(--white);display:flex;align-items:center}
.row.band.small{font-size:10.5px}
.online .icon{width:56px;display:flex;justify-content:center;border-right:1px solid #aaa;height:32px;align-items:center;margin-left:6px}
.online .info{padding-left:14px;line-height:19px;font-size:10.5px}
.simple .icon{margin-left:26px;margin-right:8px;display:flex}
.simple p{font-size:10.5px}
.totals{align-items:flex-start !important;padding-top:18px}
.totals .icon{margin-left:24px;margin-right:8px;margin-top:2px}
.totals p{font-size:10.5px;line-height:16px}
.site-footer{position:absolute;left:0;top:1078px;width:1200px;height:88px;background:var(--dark);color:#e0e0e0;font-size:10.5px}
.footer-brand{position:absolute;left:133px;top:33px;font-family:"Montserrat",sans-serif;font-weight:800;font-size:16px;color:var(--white);display:flex;align-items:center;gap:6px}
.footer-brand .dot{width:10px;height:10px;background:var(--red)}
.copyright{position:absolute;left:488px;top:38px}
.clock{position:absolute;right:132px;top:38px}
</style>
</head>
<body>
<header class="site-header">
  <div class="brand"><span class="dot"></span>QUENDRIX-COMMONS</div>
  <div class="account">
    <span class="avatar"><svg width="11" height="12" viewBox="0 0 11 12"><circle cx="5.5" cy="3.3" r="2.8" fill="#353535"/><path d="M0 12c0-4 2.5-5.5 5.5-5.5S11 8 11 12z" fill="#353535"/></svg></span>
    <span class="greeting">Welcome Guest</span>
    <span class="btn-outline">Login</span>
    <span class="btn-outline">Register</span>
  </div>
</header>
<nav class="nav"><ul><li>Help</li><li>Search</li><li>Members</li><li>Calendar</li></ul></nav>

<main class="main">
  <h1 class="page-title">
    <svg width="26" height="28" viewBox="0 0 26 28"><path d="M2 25 L20 4" stroke="#353535" stroke-width="2.6" stroke-linecap="round"/><circle cx="23" cy="4" r="2.3" fill="none" stroke="#353535" stroke-width="1.6"/><circle cx="11" cy="25" r="2.3" fill="none" stroke="#353535" stroke-width="1.6"/></svg>
    LONGBOARD
  </h1>

  <div class="welcome-bar">Welcome back; your last visit was : <em>Today, 09:41am</em>
    <div class="login-form">
      <div class="field">User Name</div>
      <div class="field pass">•••••••</div>
      <div class="go">GO</div>
    </div>
  </div>

  <div class="cat-head" style="top:266px">
    <svg width="14" height="14" viewBox="0 0 14 14"><circle cx="7" cy="7" r="6.5" fill="#fff"/><circle cx="8" cy="7" r="3.8" fill="#e2001a"/><circle cx="8.5" cy="7" r="1.6" fill="#fff"/></svg>
    A TEST ROOT<span class="collapse"></span>
  </div>

  <table class="forum-table">
    <colgroup><col style="width:590px"><col style="width:68px"><col style="width:79px"><col style="width:199px"></colgroup>
    <tr><th>Forum</th><th class="num">Topics</th><th class="num">Replies</th><th>Last Post Info</th></tr>
    <tr>
      <td><div class="forum-cell"><span class="icon"><svg width="20" height="20" viewBox="0 0 20 20"><circle cx="10" cy="10" r="9" fill="#353535"/><circle cx="11.5" cy="10" r="5.5" fill="#ececec"/><circle cx="12" cy="10" r="3.2" fill="#353535"/></svg></span>
        <div><div class="forum-name">A Test Forum</div><div>Lorem Ipsum is simply dummy text of the printing</div></div></div></td>
      <td class="num">1</td>
      <td class="num">1</td>
      <td class="last-post">April 07,2018, 7:52 PM<br><b>In :</b> Welcome<br><b>By :</b> Norvale Team</td>
    </tr>
  </table>

  <div class="board-links"><span>Delete cookies set by this board</span><span>|</span><span>Mark all posts as read</span></div>

  <div class="cat-head" style="top:505px">
    <svg width="24" height="12" viewBox="0 0 24 12"><path d="M1 2h22v3H1z" fill="#fff"/><circle cx="6" cy="9" r="2.2" fill="#fff"/><circle cx="18" cy="9" r="2.2" fill="#fff"/></svg>
    BOARD STATISTICS<span class="collapse"></span>
  </div>
  <div class="stats-nav"><span>Today's active topics</span><span class="sep"></span><span>The moderating team</span><span class="sep"></span><span>Today's top 10 posters</span><span class="sep"></span><span>Overall top 10 posters</span></div>

  <div class="row band small" style="top:563px;height:28px">2 user(s) active in the past 15 minutes</div>
  <div class="row body online" style="top:591px;height:90px">
    <span class="icon"><svg width="26" height="26" viewBox="0 0 26 26"><rect x="2" y="9" width="22" height="8" rx="4" transform="rotate(-40 13 13)" fill="#353535"/><circle cx="8" cy="20" r="2" fill="#353535"/><circle cx="20" cy="8" r="2" fill="#353535"/></svg></span>
    <div class="info"><b>2</b> guests, <b>0</b> members <b>0</b> anonymous members<br><b>Show detailed by :</b> <a href="#">Last Click</a>, <a href="#">Member Name</a></div>
  </div>

  <div class="row band" style="top:681px;height:31px">Today’s Birthdays</div>
  <div class="row body simple" style="top:712px;height:64px;align-items:flex-start;padding-top:12px">
    <span class="icon"><svg width="20" height="20" viewBox="0 0 20 20"><circle cx="10" cy="10" r="9" fill="#353535"/><circle cx="11.5" cy="10" r="5.5" fill="#fff"/><circle cx="12" cy="10" r="3.2" fill="#353535"/></svg></span>
    <p>No members are celebrating a birthday today</p>
  </div>

  <div class="row band" style="top:776px;height:32px">Forthcoming Calendar Events within the next 5 days</div>
  <div class="row body simple" style="top:808px;height:61px;align-items:flex-start;padding-top:13px">
    <span class="icon"><svg width="20" height="20" viewBox="0 0 20 20"><circle cx="10" cy="10" r="9" fill="#353535"/><circle cx="11.5" cy="10" r="5.5" fill="#fff"/><circle cx="12" cy="10" r="3.2" fill="#353535"/></svg></span>
    <p>There are no Forthcoming Calendar Events</p>
  </div>

  <div class="row band" style="top:869px;height:32px">Board Statistics</div>
  <div class="row body totals" style="top:901px;height:102px;box-shadow:0 1px 2px rgba(0,0,0,.1)">
    <span class="icon"><svg width="22" height="40" viewBox="0 0 22 40"><rect x="5" y="1" width="12" height="38" rx="6" fill="#353535"/><rect x="1" y="9" width="2" height="6" fill="#353535"/><rect x="19" y="9" width="2" height="6" fill="#353535"/><rect x="1" y="26" width="2" height="6" fill="#353535"/><rect x="19" y="26" width="2" height="6" fill="#353535"/><rect x="8" y="11" width="6" height="1.5" fill="#fff"/><rect x="8" y="28" width="6" height="1.5" fill="#fff"/></svg></span>
    <p>Oure member have made a total of <b>1</b> posts<br>We have <b>1</b> registered members<br>The newest member is <a href="#"><b>admin</b></a><br>Most users ever online was <b>2</b> on <b>Today, 08:36 AM</b></p>
  </div>
</main>

<footer class="site-footer">
  <div class="footer-brand"><span class="dot"></span>QUENDRIX-COMMONS</div>
  <div class="copyright">Copyrights @ 2018 All Rights Reserved</div>
  <div class="clock">Time is now : 6th June 2018 - 09:15 AM</div>
</footer>
</body>
</html>
```